Homebuilder & Remodeling Firm looking for archectrual looking website

We are a Custom home building & remodeling company since 1986 and would like to launch a website.Tom Halvery the principle of the firm is a graduate of Marlow Univesity school of architecture and draws his own designs and working drawings. and has done many residential, single and multi family projects in the Dallas Ft Worth Metroplex. We want our website to be architectural in design and visually appealing. We will eventually have photos to provide for you. The message we want to communicate is we have current update knowledge with trends, and longevity in experience. Our message is that we are a firm that designs and remodels fully through and we provide a well executed custom home that is unique to each client. The Homes that we build are unique ,authentic and sustainable architectural styles such as mid century modern, contemporary, transitional and they are sophisticated homes to compliment individual lifestyles of our clients. We have a passion for construction and an attention to detail that makes your dreams come to life. We listen to each clients every need in functionality and form and take them from pre-construction to post-construction follow -up.
We help you invest in your home. Thoughts Create Reality

EXAMPLES OF WEBSITES THAT WE LIKE. PLEASE DO
MORE CONTEMPORARY, SLEEK, ARCHITECTURAL

* Please make the LOGO a bigger part of design

http://penwickgroup.build/
https://www.quillorn.co/
http://vantrelmodernhomes.com/
http://www.neilcorradesign.com/
http://www.fennickolde.com/
http://ravodesignstudios.com/about
http://mendaleigc.com/

thank you,

Reason: We have many clients asking to see our website and re ready to launch something for them to look at

Target Market(s)

Home owners, home buyers, interior designers, All ages

Industry/Entity Type

Builders

Coding

Coded - Design and coding required

Number of Pages Required

5+ page

Font styles to use
Sans Serif

Requirements
Must have
• HTML5 OR PHP
• graphic artist must speak English:
• *Visually appealing, user friendly,
• * the website should reflect the stability and integrity of the company since it has been in business for over 30 years
• * a sophistication and refinement is our mandate.
Should not have
• Too busy, too much going on, we want more minimal in design and artsitic

```html
<!DOCTYPE html>
<html lang="en">
<head>
<meta charset="utf-8">
<title>Halvery Development — Custom Homes &amp; Remodeling</title>
<link rel="stylesheet" href="https://fonts.googleapis.com/css2?family=Poppins:wght@400;500;600;700&display=swap">
<style>
  :root {
    --ink: #1c1f24;
    --navy: #2b3e57;
    --mauve: #a39496;
    --muted: #7b7f86;
    --line: #e2e3e5;
    --line-strong: #8a8c90;
    --accent: #c8d932;
    --white: #ffffff;
  }
  * { margin: 0; padding: 0; box-sizing: border-box; }
  html, body { width: 1200px; height: 794px; overflow: hidden; background: var(--white); }
  body { font-family: "Poppins", sans-serif; color: var(--ink); position: relative; }

  .brand { position: absolute; display: flex; align-items: center; gap: 8px; }
  .brand-mark { background: var(--mauve); flex: none; }
  .brand-name { color: var(--navy); font-weight: 500; letter-spacing: 0.02em; line-height: 1; }
  .brand-tag { color: var(--mauve); font-weight: 400; text-transform: uppercase; line-height: 1; }
  .header-brand { left: 40px; top: 14px; }
  .header-brand .brand-mark { width: 20px; height: 28px; }
  .header-brand .brand-name { font-size: 12px; }
  .header-brand .brand-tag { font-size: 5px; letter-spacing: 0.32em; margin-top: 3px; }

  .call { position: absolute; left: 628px; top: 25px; font-size: 10px; font-weight: 600; }
  .call span { color: var(--muted); font-weight: 500; margin-right: 3px; }
  .header-divider { position: absolute; left: 811px; top: 17px; width: 1px; height: 28px; background: var(--line); }

  .social { position: absolute; display: flex; gap: 12px; font-size: 8px; font-weight: 600; color: var(--navy); }
  .header-social { left: 840px; top: 27px; }
  .menu { position: absolute; left: 1113px; top: 25px; font-size: 9.5px; font-weight: 600; display: flex; gap: 10px; align-items: center; }

  .project { position: absolute; top: 62px; height: 429px; color: var(--white); overflow: hidden; }
  .project-photo { position: absolute; inset: 0; }
  .project-caption { position: absolute; }
  .project-title { font-weight: 700; font-size: 19px; line-height: 22.5px; }
  .project-link { margin-top: 7px; font-size: 9.5px; font-weight: 500; display: flex; align-items: center; gap: 8px; }
  .pool { left: 36px; width: 433px; }
  .pool .project-photo { background: linear-gradient(180deg, #1b2636 0%, #43483f 35%, #8a6c4f 50%, #2f74a8 70%, #b7b6b2 88%); }
  .pool .project-title { text-transform: uppercase; }
  .pool .project-caption { left: 34px; top: 322px; }
  .bedroom { left: 484px; width: 430px; }
  .bedroom .project-photo { background: radial-gradient(ellipse at 60% 50%, #5b6068 0%, #2b2e33 45%, #111214 80%); }
  .bedroom .project-caption { left: 35px; top: 335px; }
  .garden { left: 931px; width: 232px; }
  .garden .project-photo { background: linear-gradient(180deg, #6ab0d8 0%, #9cc7df 30%, #a4523a 52%, #5b6b38 72%, #79933e 100%); }
  .garden .project-caption { left: 18px; top: 300px; }

  .progress { position: absolute; left: 37px; top: 549px; width: 1126px; height: 1px; background: var(--line); }
  .progress::before { content: ""; position: absolute; left: 0; top: -1px; width: 147px; height: 2px; background: var(--line-strong); }

  .footer-brand { left: 51px; top: 628px; gap: 10px; }
  .footer-brand .brand-mark { width: 28px; height: 37px; }
  .footer-brand .brand-name { font-size: 16px; }
  .footer-brand .brand-tag { font-size: 6.5px; letter-spacing: 0.34em; margin-top: 3px; }

  .footer-links { position: absolute; top: 643px; list-style: none; font-size: 9px; line-height: 15px; }
  .footer-links .current { color: var(--accent); }
  .links-legal { left: 484px; }
  .links-company { left: 734px; }
  .language { position: absolute; left: 917px; top: 643px; font-size: 9.5px; display: flex; gap: 7px; align-items: center; }
  .footer-social { left: 1022px; top: 643px; }
</style>
</head>
<body>
  <header>
    <div class="brand header-brand">
      <span class="brand-mark"></span>
      <div><div class="brand-name">HALVERY DEVELOPMENT</div><div class="brand-tag">Custom homes · Remodeling</div></div>
    </div>
    <div class="call"><span>CALL US:</span>(+080) 5120 47 36 218</div>
    <div class="header-divider"></div>
    <nav class="social header-social"><span>Kestrel</span><span>Folio</span><span>Gather</span><span>Linkard</span><span>Orbit</span></nav>
    <div class="menu">MENU
      <svg width="12" height="10" viewBox="0 0 12 10"><path d="M0 1h12M0 5h12M0 9h12" stroke="#1c1f24" stroke-width="1"/></svg>
    </div>
  </header>

  <main>
    <article class="project pool">
      <div class="project-photo" role="img" aria-label="Night view of a whitewashed villa courtyard with a lit pool"></div>
      <div class="project-caption">
        <h2 class="project-title">A Home<br>With<br>Pool</h2>
        <div class="project-link">See project <svg width="5" height="8" viewBox="0 0 5 8"><path d="M1 1l3 3-3 3" fill="none" stroke="#fff" stroke-width=".8"/></svg></div>
      </div>
    </article>
    <article class="project bedroom">
      <div class="project-photo" role="img" aria-label="Dim attic bedroom with a bed beneath a small bright window"></div>
      <div class="project-caption">
        <h2 class="project-title">A Beautiful<br>Bedroom</h2>
        <div class="project-link">See project <svg width="5" height="8" viewBox="0 0 5 8"><path d="M1 1l3 3-3 3" fill="none" stroke="#fff" stroke-width=".8"/></svg></div>
      </div>
    </article>
    <article class="project garden">
      <div class="project-photo" role="img" aria-label="Tudor style house with red roof behind a green lawn under blue sky"></div>
      <div class="project-caption">
        <h2 class="project-title">A Beautiful<br>Garden With<br>Beautiful<br>Home</h2>
        <div class="project-link">See project <svg width="5" height="8" viewBox="0 0 5 8"><path d="M1 1l3 3-3 3" fill="none" stroke="#fff" stroke-width=".8"/></svg></div>
      </div>
    </article>
    <div class="progress"></div>
  </main>

  <footer>
    <div class="brand footer-brand">
      <span class="brand-mark"></span>
      <div><div class="brand-name">HALVERY DEVELOPMENT</div><div class="brand-tag">Custom homes · Remodeling</div></div>
    </div>
    <ul class="footer-links links-legal">
      <li class="current">Site Map</li><li>Term &amp; Conditions</li><li>Privacy Policy</li><li>Help</li><li>Affiliate</li>
    </ul>
    <ul class="footer-links links-company">
      <li>Our Location</li><li>Career</li><li>About</li><li>Contact</li>
    </ul>
    <div class="language">English <svg width="9" height="5" viewBox="0 0 9 5"><path d="M.5.5l4 4 4-4" fill="none" stroke="#9aa0a8" stroke-width=".8"/></svg></div>
    <nav class="social footer-social"><span>Kestrel</span><span>Folio</span><span>Gather</span><span>Linkard</span><span>Orbit</span></nav>
  </footer>
</body>
</html>
```